8.5 x 11" Funny Poster - "In case of Alien Invasion..."

We sell data backup services to small business customers which is sometimes "too serious". We're creating a campaign to focus on a more light hearted way to draw customer's attention.
The Poster should seek to use imagery that is funny and light hearted -- be creative. It needs to draw attention and get the reader to chuckle.
Our products are sold in computer stores -- so we're looking to create an 8.5" x 11" Tabletop Sign to be displayed as an instore display. We'll be using Plintora to print the signs, their product specifications with bleeds and margins are documented on their website at:
http://www.plintora-example.com/signs-and-banners/signs/table-top-signs
The copy for the poster is attached in both Word and pdf formats. We'd like a small version of our logo to be included somewhere on the flyer (attached is a Illustrator and JPG version of our logo). We'd also like to include our url http://welbrook-example.net.
The finished product should be Adobe Illustrator CS3 (*.ai) with a PDF Proof.
Target Market(s)
retail small business
Industry/Entity Type
Business
Colors
Designer to choose colors to be used in the design.
Look and feel
Each slider illustrates characteristics of the customer's brand and the style your logo design should communicate.

```html
<!DOCTYPE html>
<html lang="en">
<head>
<meta charset="utf-8">
<title>In Case of Alien Invasion – Welbrook Net</title>
<link href="https://fonts.googleapis.com/css2?family=Francois+One&display=swap" rel="stylesheet">
<style>
  :root {
    --sky-light: #3fc3ee;
    --sky-mid: #2aa3d6;
    --sky-deep: #1a6c9e;
    --ink-white: #ffffff;
    --text-shadow: rgba(6, 50, 80, 0.45);
    --brand-dot: #5fbf3a;
  }
  html, body {
    margin: 0;
    padding: 0;
    width: 898px;
    height: 1200px;
    overflow: hidden;
    background: var(--sky-deep);
  }
  .poster {
    position: relative;
    width: 898px;
    height: 1200px;
    overflow: hidden;
    background: radial-gradient(ellipse 75% 65% at 50% 48%, var(--sky-light) 0%, var(--sky-mid) 55%, var(--sky-deep) 100%);
    font-family: "Francois One", "Arial Narrow", sans-serif;
    color: var(--ink-white);
    text-transform: uppercase;
  }
  .headline-line {
    position: absolute;
    left: 0;
    width: 100%;
    margin: 0;
    text-align: center;
    line-height: 1;
    font-weight: 400;
    text-shadow: 2px 3px 3px var(--text-shadow);
    white-space: nowrap;
  }
  .line-invasion { top: 58px; font-size: 58px; letter-spacing: 1px; }
  .line-save-kids { top: 128px; font-size: 49px; letter-spacing: 1px; }
  .line-computer { top: 192px; font-size: 66px; letter-spacing: 1px; }
  .line-leave { top: 268px; font-size: 96px; letter-spacing: 2px; }
  .line-second { top: 732px; font-size: 76px; letter-spacing: 1px; }
  .line-backup { top: 818px; font-size: 57px; letter-spacing: 1px; }
  .line-forget { top: 892px; font-size: 56px; letter-spacing: 1px; }
  .line-save-granny { top: 962px; font-size: 100px; letter-spacing: 2px; }

  .saucer-fleet {
    position: absolute;
    left: 40px;
    top: 450px;
    width: 818px;
    height: 210px;
    border-radius: 40px;
    background: radial-gradient(ellipse at 50% 50%, rgba(255,255,255,0.22), rgba(255,255,255,0.04) 70%);
  }

  .sponsor-footer {
    position: absolute;
    left: 30px;
    right: 30px;
    top: 1110px;
    display: flex;
    align-items: center;
    gap: 22px;
  }
  .brand-mark {
    display: flex;
    align-items: center;
    gap: 10px;
    font-size: 44px;
    line-height: 1;
    text-transform: none;
    color: var(--ink-white);
  }
  .brand-dot {
    width: 30px;
    height: 30px;
    border-radius: 50%;
    background: var(--brand-dot);
  }
  .sponsor-lines {
    line-height: 1.15;
    text-shadow: 1px 2px 2px var(--text-shadow);
  }
  .sponsor-credit { font-size: 24px; letter-spacing: 0.5px; }
  .sponsor-tagline { font-size: 17px; letter-spacing: 0.5px; }
</style>
</head>
<body>
  <main class="poster">
    <p class="headline-line line-invasion">In case of alien invasion</p>
    <p class="headline-line line-save-kids">Save the children, the pets</p>
    <p class="headline-line line-computer">And your computer</p>
    <p class="headline-line line-leave">Leave Granny</p>

    <div class="saucer-fleet" role="img" aria-label="A fleet of white flying saucers of different sizes"></div>

    <p class="headline-line line-second">On second thought</p>
    <p class="headline-line line-backup">Backup with Welbrook Net,</p>
    <p class="headline-line line-forget">And forget the computer</p>
    <p class="headline-line line-save-granny">Save Granny!</p>

    <footer class="sponsor-footer">
      <div class="brand-mark">
        <span>Welbrook Net</span>
        <span class="brand-dot" aria-hidden="true"></span>
      </div>
      <div class="sponsor-lines">
        <div class="sponsor-credit">Brought to you by Welbrook Net, Inc.</div>
        <div class="sponsor-tagline">Saving the planet from alien invasion since 1994.</div>
      </div>
    </footer>
  </main>
</body>
</html>
```